Create a memorable Web Design for real estate branding

we are a Minnepolis brokerage and boutique housing specialist with over 27 years of experience in the Global furnished housing industry, servicing the Greater Los Angeles area. Specializing in “warm environments” we offer a customized approach to satisfying our guests and client’s needs by offering a wide array of options in highly desirable areas. Additionally, Lantern Dwelling Partners offers assistance and expertise to home buyers, sellers and investors.

Industry/Entity Type

Real Estate

Number of Pages Required

1 page

Font styles to use
Serif
Sans Serif
Decorative

```html
<!DOCTYPE html>
<html lang="en">
<head>
<meta charset="utf-8">
<title>Lantern Dwelling Partners — Real Estate</title>
<link rel="stylesheet" href="https://fonts.googleapis.com/css2?family=Open+Sans:wght@400;600;700&family=Pacifico&family=Marcellus&family=Arimo:wght@400;700&display=swap">
<style>
:root{
  --header:#2a2a2a;
  --header-top:#3a3a3a;
  --accent-green:#a6d44a;
  --logo:#3fbf9a;
  --welcome-bg:#d5ef9f;
  --wave-green:#c2e57a;
  --grey-bg:#f0f0f0;
  --blue-bg:#d7e6f3;
  --link-blue:#3a9ad9;
  --search-btn:#a9c9ef;
  --footer:#121212;
  --teal:#3cc3a3;
  --bar:#19a98a;
  --text:#111;
  --muted:#8a8a8a;
  --avatar:#a9b6c2;
  --white:#fff;
}
*{margin:0;padding:0;box-sizing:border-box}
html,body{width:682px;height:1200px;overflow:hidden}
body{position:relative;font-family:"Open Sans",Arial,sans-serif;color:var(--text);background:var(--grey-bg)}
.abs{position:absolute}

/* header */
.site-header{left:0;top:0;width:682px;height:66px;background:linear-gradient(var(--header-top),var(--header))}
.brand{left:57px;top:14px;color:var(--logo);font-weight:700;font-size:19px;line-height:20px;letter-spacing:.5px}
.brand small{display:block;font-size:12px;font-weight:700;letter-spacing:2px}
.enquiry{right:54px;top:10px;font-size:10px;color:var(--white)}
.enquiry span{color:var(--accent-green);margin-left:8px}
.main-nav{left:239px;top:33px;display:flex;gap:0;font-size:9.6px;color:var(--white)}
.main-nav a{color:inherit;text-decoration:none;position:absolute;white-space:nowrap}
.main-nav a.current{color:var(--accent-green)}

/* hero */
.hero{left:0;top:66px;width:682px;height:274px;background:linear-gradient(180deg,#c9d7e3 0%,#e6e2d6 38%,#9a9a86 62%,#6f8a4a 82%,#556b34 100%)}
.search-panel{left:141px;top:226px;width:426px;height:76px;background:rgba(30,30,30,.75)}
.search-input{left:13px;top:16px;width:296px;height:18px;background:var(--white);font-size:8.5px;padding:3px 8px;color:#333}
.search-btn{left:322px;top:16px;width:90px;height:18px;background:var(--search-btn);font-size:8.5px;text-align:center;line-height:18px;color:#222}
.select{top:44px;height:16px;background:var(--white);font-size:8.5px;line-height:16px;padding-left:7px;color:#333}
.select::after{content:"";position:absolute;right:7px;top:5px;width:4px;height:4px;border-right:1px solid #555;border-bottom:1px solid #555;transform:rotate(45deg)}
.dots{left:139px;top:322px;display:flex;gap:4px}
.dots i{width:8px;height:8px;border-radius:50%;background:#ddd;display:block}
.dots i.on{background:#e0201c}

/* welcome */
.welcome{left:0;top:340px;width:682px;height:180px;background:var(--welcome-bg)}
.social{width:17px;height:17px;border-radius:50%;background:#9a9a9a;top:349px}
.account{top:352px;font-size:10px;color:#222}
.account-sep{left:523px;top:351px;width:1px;height:14px;background:#777}
.welcome-title{left:88px;top:366px;font-family:"Pacifico",cursive;font-size:13px}
.welcome-copy{left:88px;top:391px;width:530px;font-size:11.2px;line-height:12.8px}
.know-more{left:86px;top:456px;font-size:9.6px;font-weight:600;display:flex;align-items:center;gap:7px}

/* properties */
.section-title{right:74px;top:500px;font-family:"Marcellus",serif;font-size:16.5px;color:#222}
.card{top:536px;width:125px;height:142px;background:var(--white);box-shadow:0 0 3px rgba(0,0,0,.18)}
.card .photo{position:absolute;left:4px;top:4px;width:117px;height:118px}
.card .meta{position:absolute;left:9px;right:9px;top:126px;display:flex;justify-content:space-between;font-size:8px}
.card .place{color:var(--muted)}
.card .price{color:var(--link-blue)}
.view-more{right:68px;top:686px;font-size:9.6px;font-weight:600}

/* news and agents */
.lower{left:0;top:705px;width:682px;height:300px;background:var(--blue-bg);border-top:1px solid #e2e8ee}
.col-title{top:729px;font-size:11.5px;font-weight:700}
.more-link{top:731px;font-size:5.5px;color:var(--link-blue)}
.rule{height:1px;background:#c0cfdc}
.news-thumb{left:84px;width:55px;height:55px;border:2px solid #b9c3cb;background:linear-gradient(180deg,#dfe7ee,#b59c7d 60%,#6e8a46)}
.news-item{left:151px;width:148px;font-size:9.2px;line-height:10.4px}
.news-item h3{font-size:8.6px;font-weight:700;margin-left:2px}
.read-more{display:block;text-align:right;font-size:6px;margin-top:2px}
.read-more.hot{color:#e0201c}
.divider{left:347px;top:730px;width:1px;height:216px;background:#bccbd8}
.avatar{left:400px;width:49px;height:49px;background:var(--avatar)}
.agent{left:461px;width:130px;font-size:7.6px;line-height:9px}
.agent h3{font-size:7.6px;font-weight:700;margin-bottom:2px}

/* footer */
.footer{left:0;top:985px;width:682px;height:181px;background:var(--footer)}
.foot-h{top:1021px;font-family:"Arimo",Arial,sans-serif;font-weight:700;font-size:9.4px;color:var(--teal)}
.foot-list{font-family:"Arimo",Arial,sans-serif;font-size:8.2px;color:var(--white);line-height:13.4px}
.contact-row{left:93px;font-family:"Arimo",Arial,sans-serif;font-size:8.2px;color:var(--white);display:flex;align-items:center;gap:9px}
.foot-social{top:1128px;width:12px;height:12px;border-radius:50%;background:#9a9a9a}
.email-field{left:499px;top:1068px;width:122px;height:14px;background:#c8c8c8;font-size:8px;color:#666;padding-left:20px;line-height:14px}
.subscribe{left:567px;top:1088px;width:54px;height:14px;background:var(--accent-green);font-size:8.5px;text-align:center;line-height:14px;color:#222}
.bottom-bar{left:0;top:1166px;width:682px;height:34px;background:var(--bar);color:var(--white);text-align:center;font-family:"Arimo",Arial,sans-serif;font-weight:700;font-size:6.4px;line-height:8px;padding-top:8px}
</style>
</head>
<body>

<header class="site-header abs">
  <div class="brand abs">Lantern Dwelling<small>PARTNERS</small></div>
  <div class="enquiry abs">Make an Enquiry <span>+0123 456 789</span></div>
  <nav class="main-nav abs">
    <a class="current" style="left:0">Home</a>
    <a style="left:42px">Buyers</a>
    <a style="left:90px">Owners</a>
    <a style="left:142px">Sellers</a>
    <a style="left:190px">Agents</a>
    <a style="left:238px">Maps</a>
    <a style="left:277px">Services</a>
    <a style="left:328px">Contact Us</a>
  </nav>
</header>

<section class="hero abs" role="img" aria-label="Photo of large modern timber-clad family houses on a green lawn under a pale sky"></section>
<div class="search-panel abs">
  <div class="search-input abs">Type here...</div>
  <div class="search-btn abs">Search</div>
  <div class="select abs" style="left:13px;width:57px">For Sale</div>
  <div class="select abs" style="left:82px;width:90px">Location</div>
  <div class="select abs" style="left:185px;width:88px">Type</div>
  <div class="select abs" style="left:287px;width:56px">Beds</div>
  <div class="select abs" style="left:356px;width:56px">Baths</div>
</div>
<div class="dots abs"><i></i><i class="on"></i><i></i><i></i></div>
<svg class="abs" style="left:332px;top:308px" width="62" height="28" viewBox="0 0 62 28">
  <g fill="none" stroke="#eee" stroke-width="1.2">
    <circle cx="14" cy="14" r="12.5"/><polyline points="17,8 11,14 17,20"/>
    <circle cx="45" cy="14" r="12.5"/><polyline points="42,8 48,14 42,20"/>
  </g>
</svg>

<section class="welcome abs"></section>
<svg class="abs" style="left:0;top:455px" width="682" height="60" viewBox="0 0 682 60">
  <path d="M0 20 C60 50 140 60 240 45 C380 22 520 5 682 10 L682 60 L0 60 Z" fill="var(--wave-green)"/>
  <path d="M0 28 C70 55 150 60 250 50 C390 30 520 14 682 18 L682 60 L0 60 Z" fill="var(--grey-bg)"/>
</svg>
<span class="social abs" style="left:430px"></span>
<span class="social abs" style="left:452px"></span>
<span class="account abs" style="left:489px">Log In</span>
<span class="account-sep abs"></span>
<span class="account abs" style="left:531px">Register</span>
<h1 class="welcome-title abs">Welcome to Lantern Dwelling</h1>
<p class="welcome-copy abs">Lorem Ipsum is simply dummy text of the printing and typesetting industry. Lorem Ipsum has been the industry's standard dummy text ever since the 1500s, when an unknown printer took a galley of type and scrambled it to make a type specimen book. It has survived not only five centuries, but also the leap into electronic typesetting, remaining essentially unchanged.</p>
<div class="know-more abs">
  <svg width="21" height="21" viewBox="0 0 21 21"><g fill="none" stroke="#222" stroke-width="1.1"><circle cx="10.5" cy="10.5" r="9.8"/><polyline points="7,6.5 11,10.5 7,14.5"/><polyline points="10.5,6.5 14.5,10.5 10.5,14.5"/></g></svg>
  KNOW MORE
</div>

<h2 class="section-title abs">Property &amp; Real Estate for Sale and Rent</h2>
<article class="card abs" style="left:82px"><div class="photo" role="img" aria-label="Photo of a glass-walled villa with a lit pool at dusk" style="background:linear-gradient(180deg,#5a6f9a,#c79a6a 55%,#4aa3c8 80%,#7a5a40)"></div><div class="meta"><span class="place">&#9679; Place</span><span class="price">Price</span></div></article>
<article class="card abs" style="left:216px"><div class="photo" role="img" aria-label="Photo of a timber-clad family house on a lawn" style="background:linear-gradient(180deg,#c6d6e4,#d9d3c6 50%,#8c7a60 75%,#6d8a45)"></div><div class="meta"><span class="place">&#9679; Place</span><span class="price">Price</span></div></article>
<article class="card abs" style="left:352px"><div class="photo" role="img" aria-label="Aerial photo of a modern hillside house with an infinity pool" style="background:linear-gradient(160deg,#5e7e3c,#b7a78a 45%,#4fb6d6 65%,#9a8a70)"></div><div class="meta"><span class="place">&#9679; Place</span><span class="price">Price</span></div></article>
<article class="card abs" style="left:488px"><div class="photo" role="img" aria-label="Photo of a resort apartment block beside a turquoise pool" style="background:linear-gradient(180deg,#6fa3d8,#d8cfc0 45%,#6ccfd2 70%,#3fb8c4)"></div><div class="meta"><span class="place">&#9679; Place</span><span class="price">Price</span></div></article>
<div class="view-more abs">VIEW MORE</div>

<section class="lower abs"></section>
<h2 class="col-title abs" style="left:84px">Industry News</h2>
<span class="more-link abs" style="left:241px">More News</span>
<svg class="abs" style="left:276px;top:725px" width="20" height="20" viewBox="0 0 20 20"><g fill="none" stroke="var(--link-blue)" stroke-width="1.1"><circle cx="10" cy="10" r="9.2"/><polyline points="8,5.5 12.5,10 8,14.5"/></g></svg>
<div class="rule abs" style="left:84px;top:750px;width:212px"></div>

<div class="news-thumb abs" style="top:755px" role="img" aria-label="Thumbnail photo of a family house"></div>
<div class="news-item abs" style="top:756px"><h3>TITLE GOES HERE</h3>Lorem Ipsum is simply dummy text of the printing and typesetting industry. Lorem Ipsum has been the industry's standard dummy<span class="read-more hot">Read More..</span></div>
<div class="news-thumb abs" style="top:824px" role="img" aria-label="Thumbnail photo of a family house"></div>
<div class="news-item abs" style="top:824px"><h3>TITLE GOES HERE</h3>Lorem Ipsum is simply dummy text of the printing and typesetting industry. Lorem Ipsum has been the industry's standard<span class="read-more">Read More..</span></div>
<div class="news-thumb abs" style="top:892px" role="img" aria-label="Thumbnail photo of a family house"></div>
<div class="news-item abs" style="top:891px"><h3>TITLE GOES HERE</h3>Lorem Ipsum is simply dummy text of the printing and typesetting industry. Lorem Ipsum has been the industry's standard<span class="read-more">Read More..</span></div>

<div class="divider abs"></div>

<h2 class="col-title abs" style="left:401px">Agents</h2>
<span class="more-link abs" style="left:552px">All Agents</span>
<svg class="abs" style="left:592px;top:725px" width="20" height="20" viewBox="0 0 20 20"><g fill="none" stroke="var(--link-blue)" stroke-width="1.1"><circle cx="10" cy="10" r="9.2"/><polyline points="8,5.5 12.5,10 8,14.5"/></g></svg>
<div class="avatar abs" style="top:755px"></div>
<div class="agent abs" style="top:756px"><h3>Name</h3>Lorem Ipsum is simply dummy text of the printing and typesetting industry. Lorem Ipsum has been the industry's standard dummy</div>
<div class="rule abs" style="left:400px;top:815px;width:214px"></div>
<div class="avatar abs" style="top:826px"></div>
<div class="agent abs" style="top:827px"><h3>Name</h3>Lorem Ipsum is simply dummy text of the printing and typesetting industry. Lorem Ipsum has been the industry's standard</div>
<div class="rule abs" style="left:400px;top:887px;width:214px"></div>
<div class="avatar abs" style="top:897px"></div>
<div class="agent abs" style="top:898px"><h3>Name</h3>Lorem Ipsum is simply dummy text of the printing and typesetting industry. Lorem Ipsum has been the industry's standard</div>

<footer class="footer abs"></footer>
<svg class="abs" style="left:0;top:955px" width="682" height="45" viewBox="0 0 682 45">
  <path d="M0 20 C90 45 220 48 340 35 C470 20 580 5 682 12 L682 45 L0 45 Z" fill="#ffffff"/>
  <path d="M0 24 C90 48 220 50 340 38 C470 24 580 10 682 16 L682 45 L0 45 Z" fill="var(--footer)"/>
</svg>

<h3 class="foot-h abs" style="left:93px">CONTACT US</h3>
<h3 class="foot-h abs" style="left:260px">CUSTOMER SERVICE</h3>
<h3 class="foot-h abs" style="left:393px">QUICK LINKS</h3>
<h3 class="foot-h abs" style="left:499px">NEWS LETTER SIGN UP</h3>

<div class="contact-row abs" style="top:1047px"><svg width="10" height="14" viewBox="0 0 10 14"><path d="M5 0a5 5 0 0 1 5 5c0 3.5-5 9-5 9S0 8.5 0 5a5 5 0 0 1 5-5z" fill="var(--teal)"/><circle cx="5" cy="5" r="1.8" fill="var(--footer)"/></svg>Your Address Goes Here</div>
<div class="contact-row abs" style="top:1082px"><svg width="11" height="11" viewBox="0 0 11 11"><path d="M2 0l2.2 2.6-1.2 1.6c.8 1.6 2 2.8 3.6 3.6l1.6-1.2L11 8.8 9.6 11C4.5 10.6.4 6.5 0 1.4z" fill="var(--teal)"/></svg>+0123 456 789</div>
<div class="contact-row abs" style="top:1105px"><svg width="11" height="8" viewBox="0 0 11 8"><rect width="11" height="8" fill="var(--teal)"/><polyline points="0,0 5.5,4.5 11,0" fill="none" stroke="var(--footer)" stroke-width="1"/></svg>Youremailaddressgoeshere</div>
<span class="foot-social abs" style="left:93px"></span>
<span class="foot-social abs" style="left:113px"></span>

<ul class="foot-list abs" style="left:260px;top:1046px;list-style:none">
  <li>Lorem Ipsum</li><li>Lorem Ipsum</li><li>Lorem Ipsum</li><li>Lorem Ipsum</li><li>Lorem Ipsum</li><li>Lorem Ipsum</li><li>Lorem Ipsum</li>
</ul>
<ul class="foot-list abs" style="left:394px;top:1046px;list-style:none">
  <li>Faq</li><li>New</li><li>About Us</li><li>Privacy Policy</li><li>Terms of Use</li>
</ul>
<p class="foot-list abs" style="left:500px;top:1047px;font-size:8.6px">Subscribe to our News Letter</p>
<div class="email-field abs">E-mail<svg class="abs" style="left:5px;top:3px" width="11" height="8" viewBox="0 0 11 8"><rect width="11" height="8" fill="#888"/><polyline points="0,0 5.5,4.5 11,0" fill="none" stroke="#c8c8c8" stroke-width="1"/></svg></div>
<div class="subscribe abs">Subscribe</div>

<div class="bottom-bar abs">HOME | SITE MAP | POLICIES | ARTICLES | CONTACT US | PRINT THIS PAGE | RSS rss | TOP OF PAGE<br>COPYRIGHT © 2016 Lantern Dwelling Partners</div>

</body>
</html>
```